Cover for Inspirational Daily Journal

This is the cover for a daily journal that will focus on inspirational content for black women. The cover should have a picture or silhouette of a black woman with a crown. The title is: "Grace in Bloom: A Year of Bright Mornings." The back won't have any words. Also the journal will be published on Pagewick.

```html
<!DOCTYPE html>
<html lang="en">
<head>
<meta charset="UTF-8">
<title>Grace in Bloom: A Year of Bright Mornings — Cover</title>
<link href="https://fonts.googleapis.com/css2?family=Cinzel:wght@700;900&display=swap" rel="stylesheet">
<style>
  :root {
    --ink-white: #ffffff;
    --amber: #b8651f;
    --moon-core: #fbe6a2;
    --moon-glow: #f0c35a;
    --dusk: #8a5524;
    --night: #2c1c0d;
    --deep: #140d06;
  }
  html, body {
    margin: 0;
    padding: 0;
    width: 843px;
    height: 1200px;
    overflow: hidden;
    background: var(--deep);
  }
  .cover {
    position: relative;
    width: 843px;
    height: 1200px;
    overflow: hidden;
    font-family: "Cinzel", Georgia, serif;
  }
  .cover-art {
    position: absolute;
    inset: 0;
    background:
      linear-gradient(to bottom, rgba(20,13,6,0) 55%, rgba(20,13,6,0.55) 80%, rgba(20,13,6,0.85) 100%),
      radial-gradient(circle at 49% 37%,
        var(--moon-core) 0%,
        #f6d680 16%,
        var(--moon-glow) 25%,
        #c7883a 30%,
        var(--dusk) 36%,
        #4a2f14 50%,
        var(--night) 70%,
        var(--deep) 100%);
  }
  .title {
    position: absolute;
    left: 0;
    right: 0;
    top: 392px;
    margin: 0;
    text-align: center;
    font-weight: 700;
    font-size: 100px;
    line-height: 100px;
    color: var(--ink-white);
    text-transform: uppercase;
  }
  .title span { display: block; }
  .title .title-accent { color: var(--amber); }
  .title .title-last { padding-left: 10px; }
  .rule {
    position: absolute;
    left: 0;
    width: 843px;
    height: 8px;
  }
  .rule-top { top: 992px; }
  .rule-bottom { top: 1081px; }
  .subtitle {
    position: absolute;
    left: 0;
    right: 0;
    top: 1022px;
    margin: 0;
    text-align: center;
    font-weight: 700;
    font-size: 31px;
    line-height: 40px;
    color: var(--ink-white);
    text-transform: uppercase;
  }
</style>
</head>
<body>
  <main class="cover">
    <div class="cover-art" role="img" aria-label="Silhouette of a crowned Black woman with long flowing hair and a sheer veil, seen from behind, standing in a field before a glowing full moon"></div>

    <h1 class="title">
      <span class="title-first">Grace</span>
      <span class="title-accent">in</span>
      <span class="title-last">Bloom</span>
    </h1>

    <svg class="rule rule-top" viewBox="0 0 843 8" aria-hidden="true">
      <polygon points="0,4 20,1.5 823,1.5 843,4 823,6.5 20,6.5" fill="var(--amber)"/>
    </svg>
    <p class="subtitle">A Year of Bright Mornings.</p>
    <svg class="rule rule-bottom" viewBox="0 0 843 8" aria-hidden="true">
      <polygon points="0,4 20,1.5 823,1.5 843,4 823,6.5 20,6.5" fill="var(--amber)"/>
    </svg>
  </main>
</body>
</html>
```